Harbourline Refrigeration business card design

We would like a new design for our business card as we have a new logo.
We need generic business card to give our customers with our office details - with the option of making it individualized for each manager

Target Market(s)

Companies and homeowners

Industry/Entity Type

Air Conditioning

Contact Information for Business Card

We are not sure if we want single or double sided it will depend on the design we choose

Colors
33a6d7
0255a3

Requirements
Must have
• Logo
• phone: (08) 8721 5940
• email: harbourserve@tealnet.example
• website: www.harbourlinerefrigeration.example
• AU61420
• BLD472913
Nice to have
• Address - Shed 5/284 Tallis Rd, Brackenfield SA 5731

```html
<!DOCTYPE html>
<html lang="en">
<head>
<meta charset="utf-8">
<title>Harbourline Refrigeration – Business Card</title>
<link href="https://fonts.googleapis.com/css2?family=Oswald:wght@400;500;600&display=swap" rel="stylesheet">
<style>
  :root {
    --stage: #2ea0d0;
    --brand-light: #33a6d7;
    --brand-dark: #0255a3;
    --band-light: #a8d2ec;
    --paper: #f4f5f5;
    --text-grey: #8a8c8e;
    --white: #ffffff;
  }
  * { box-sizing: border-box; margin: 0; padding: 0; }
  html, body { width: 1200px; height: 1200px; overflow: hidden; }
  body {
    background: var(--stage);
    font-family: "Oswald", sans-serif;
    position: relative;
  }
  .card {
    position: absolute;
    left: 150px;
    width: 900px;
    height: 514px;
    overflow: hidden;
    box-shadow: 0 10px 30px rgba(0, 40, 80, .25);
  }
  .card--front { top: 50px; background: var(--paper); }
  .card--back { top: 630px; background: var(--band-light); }

  /* front: brand panel */
  .brand {
    position: absolute; left: 0; top: 0; width: 300px; height: 100%;
    display: flex; align-items: center; justify-content: center; gap: 12px;
  }
  .brand__mark { width: 34px; height: 34px; border-radius: 50%; background: var(--brand-light); flex: none; }
  .brand__name { font-weight: 500; font-size: 40px; color: var(--brand-dark); letter-spacing: .5px; }

  .divider { position: absolute; left: 318px; top: 0; width: 44px; height: 100%; }
  .divider__dark { position: absolute; left: 0; width: 22px; background: var(--brand-dark); }
  .divider__dark--top { top: 0; height: 90px; }
  .divider__dark--bottom { bottom: 0; height: 80px; left: 22px; }
  .divider__light { position: absolute; left: 22px; top: 90px; width: 22px; bottom: 80px; background: var(--band-light); }

  /* front: identity */
  .identity { position: absolute; left: 410px; top: 46px; }
  .identity__name { font-weight: 500; font-size: 44px; color: var(--brand-dark); line-height: 1; }
  .identity__role { font-weight: 400; font-size: 24px; color: var(--text-grey); margin-top: 8px; }
  .rule { position: absolute; left: 410px; top: 160px; width: 300px; height: 3px; background: var(--brand-dark); }

  .licence {
    position: absolute; right: 0; height: 34px; width: 190px;
    color: var(--white); font-weight: 500; font-size: 20px;
    display: flex; align-items: center; padding-left: 34px;
    clip-path: polygon(16px 0, 100% 0, 100% 100%, 16px 100%, 0 50%);
  }
  .licence--au { top: 106px; background: var(--brand-light); }
  .licence--bld { top: 144px; background: var(--brand-dark); }

  /* front: contact list */
  .contacts { position: absolute; left: 410px; top: 200px; list-style: none; }
  .contact { display: flex; align-items: center; height: 56px; margin-bottom: 18px; }
  .contact__icon {
    width: 52px; height: 52px; border-radius: 9px; background: var(--brand-dark);
    display: flex; align-items: center; justify-content: center; flex: none;
  }
  .contact__icon svg { width: 28px; height: 28px; }
  .contact__text { margin-left: 30px; font-size: 21px; color: var(--text-grey); line-height: 1.25; white-space: nowrap; }

  /* back */
  .back__pattern { position: absolute; inset: 0; background: linear-gradient(135deg, #b4d9ef, #9fcbe8); }
  .back__badge {
    position: absolute; left: 50%; top: 50%; transform: translate(-50%, -50%);
    background: var(--white); border-radius: 70px; height: 140px; padding: 0 60px 0 40px;
    display: flex; align-items: center; gap: 26px;
  }
  .back__mark { width: 80px; height: 80px; border-radius: 50%; background: var(--brand-light); flex: none; }
  .back__name { font-weight: 500; font-size: 72px; color: var(--brand-dark); }
</style>
</head>
<body>
  <section class="card card--front">
    <div class="brand">
      <span class="brand__mark"></span>
      <span class="brand__name">Harbourline</span>
    </div>
    <div class="divider">
      <span class="divider__dark divider__dark--top"></span>
      <span class="divider__light" role="img" aria-label="Light blue diagonal stripe texture"></span>
      <span class="divider__dark divider__dark--bottom"></span>
    </div>

    <div class="identity">
      <h1 class="identity__name">JORDAN ELLIS REED</h1>
      <p class="identity__role">GRAPHIC DESIGNER</p>
    </div>
    <div class="rule"></div>
    <div class="licence licence--au">AU61420</div>
    <div class="licence licence--bld">BLD472913</div>

    <ul class="contacts">
      <li class="contact">
        <span class="contact__icon"><svg viewBox="0 0 24 24" fill="none" stroke="#fff" stroke-width="2" stroke-linejoin="round"><path d="M5 3h4l2 5-2.5 1.5a11 11 0 0 0 6 6L16 13l5 2v4a2 2 0 0 1-2 2A17 17 0 0 1 3 5a2 2 0 0 1 2-2z"/></svg></span>
        <span class="contact__text">(08) 8721 5940</span>
      </li>
      <li class="contact">
        <span class="contact__icon"><svg viewBox="0 0 24 24" fill="none" stroke="#fff" stroke-width="2"><rect x="3" y="5" width="18" height="14" rx="1"/><path d="M3 6l9 7 9-7"/></svg></span>
        <span class="contact__text">harbourserve@tealnet.example</span>
      </li>
      <li class="contact">
        <span class="contact__icon"><svg viewBox="0 0 24 24" fill="none" stroke="#fff" stroke-width="1.6"><circle cx="12" cy="12" r="9"/><ellipse cx="12" cy="12" rx="4" ry="9"/><path d="M3 12h18M5 7h14M5 17h14"/></svg></span>
        <span class="contact__text">www.harbourlinerefrigeration.example</span>
      </li>
      <li class="contact">
        <span class="contact__icon"><svg viewBox="0 0 24 24" fill="#fff"><path d="M12 2a7 7 0 0 0-7 7c0 5 7 13 7 13s7-8 7-13a7 7 0 0 0-7-7zm0 9.5A2.5 2.5 0 1 1 12 6.5a2.5 2.5 0 0 1 0 5z"/></svg></span>
        <span class="contact__text">Shed 5/284 Tallis Rd,<br>Brackenfield SA 5731</span>
      </li>
    </ul>
  </section>

  <section class="card card--back">
    <div class="back__pattern" role="img" aria-label="Fine light blue diagonal dotted texture"></div>
    <div class="back__badge">
      <span class="back__mark"></span>
      <span class="back__name">Harbourline</span>
    </div>
  </section>
</body>
</html>
```